Business Card Design Project - bel soravin group

dear Sirs

we need business card design for our group ( BEL Soravin Group ) , i have got the Logo design of our group from pixel harbor in previous , so all need details relating to our group i think available with you, as well as the the chosen logo design

we hope to provide us with business card logo that to be appropaite and satisfactory to us .

thanks

note : logo design of our group is attached .
Updates

Reason: please extend the deadline of my project for additional 15 days because i didn't received appropriate design for our gruop yet . kindly beaware that i have received 77 design till now , supossed to send me 200-250 design at least . thanks

Target Market(s)

contents
-

name : Korvan EL Mistrani

position : Operation Manager

Industry/Entity Type

Business

Requirements
Must have

• person name

group logo
Nice to have
• logo color matching with back background

```html
<!DOCTYPE html>
<html lang="en">
<head>
<meta charset="utf-8">
<title>BEL Soravin Group – Business Card</title>
<link href="https://fonts.googleapis.com/css2?family=Questrial&family=Open+Sans:ital,wght@0,400;0,600;1,400&display=swap" rel="stylesheet">
<style>
  :root{
    --backdrop:#e4e4e2;
    --card:#ffffff;
    --navy:#1f3d7f;
    --navy-deep:#142a5c;
    --gold:#c9a030;
    --ink:#2c2c2c;
    --soft-ink:#4a4a4a;
  }
  *{margin:0;padding:0;box-sizing:border-box}
  html,body{width:1200px;height:944px;overflow:hidden;background:var(--backdrop)}
  .canvas{position:relative;width:1200px;height:944px}
  .card{position:absolute;width:600px;height:343px;background:var(--card);border-radius:22px;overflow:hidden;box-shadow:0 6px 18px rgba(0,0,0,.18)}
  .card--front{left:90px;top:120px}
  .card--back{left:510px;top:500px}

  .brand{display:flex;align-items:center;gap:14px;font-family:"Questrial",sans-serif;color:var(--navy);letter-spacing:.02em;white-space:nowrap}
  .brand__mark{background:var(--navy);flex:none}
  .card--front .brand{position:absolute;left:70px;top:110px;font-size:46px}
  .card--front .brand__mark{width:22px;height:22px}
  .card--front .web{position:absolute;left:70px;top:210px;font-family:"Open Sans",sans-serif;font-size:17px;letter-spacing:.08em;color:var(--gold)}

  .card--back .brand{position:absolute;left:150px;top:44px;font-size:34px}
  .card--back .brand__mark{width:16px;height:16px}
  .holder{position:absolute;left:70px;top:118px;font-family:"Open Sans",sans-serif}
  .holder__name{font-size:20px;color:var(--ink);letter-spacing:.02em}
  .holder__role{font-size:15px;font-style:italic;color:var(--gold);margin-top:2px}

  .contact{position:absolute;font-family:"Open Sans",sans-serif;font-size:15px;color:var(--ink);list-style:none;line-height:21px}
  .contact--address{left:52px;top:190px}
  .contact--lines{left:330px;top:182px}
  .contact li{display:flex;align-items:flex-start;gap:8px}
  .contact svg{flex:none;width:14px;height:14px;margin-top:3px}
  .contact .accent{color:var(--gold)}
  .address-lines{display:block}

  .band{position:absolute;left:0;right:0;bottom:0;height:36px}
  .band__rule{position:absolute;left:0;right:0;top:0;height:4px;background:var(--gold)}
  .band__fill{position:absolute;left:0;right:0;top:6px;bottom:0;background:linear-gradient(180deg,var(--navy) 0%,var(--navy-deep) 100%)}
</style>
</head>
<body>
<main class="canvas">

  <section class="card card--front" aria-label="Card front">
    <div class="brand"><span class="brand__mark"></span><span>BEL Soravin Group</span></div>
    <p class="web">www.belsoravingroup.com</p>
  </section>

  <section class="card card--back" aria-label="Card back">
    <div class="brand"><span class="brand__mark"></span><span>BEL Soravin Group</span></div>

    <div class="holder">
      <p class="holder__name">Korvan EL Mistrani</p>
      <p class="holder__role">Operation Manager</p>
    </div>

    <ul class="contact contact--address">
      <li>
        <svg viewBox="0 0 14 14" aria-hidden="true"><path d="M7 1 1 6.5h2V13h3V9h2v4h3V6.5h2z" fill="var(--gold)"/></svg>
        <span class="address-lines">4100 Marlow Crest Blvd.<br>Suite 210-114<br>Denford, TX 78114</span>
      </li>
    </ul>

    <ul class="contact contact--lines">
      <li>
        <svg viewBox="0 0 14 14" aria-hidden="true"><path d="M3 1h3l1 3-2 1.5a7 7 0 0 0 3.5 3.5L10 7l3 1v3a2 2 0 0 1-2 2A10 10 0 0 1 1 3a2 2 0 0 1 2-2z" fill="var(--gold)"/></svg>
        <span>512-555-0142</span>
      </li>
      <li>
        <svg viewBox="0 0 14 14" aria-hidden="true"><rect x="1" y="5" width="12" height="7" rx="1" fill="var(--gold)"/><rect x="3.5" y="1.5" width="7" height="4" fill="none" stroke="var(--gold)" stroke-width="1.2"/></svg>
        <span>512-555-0143</span>
      </li>
      <li>
        <svg viewBox="0 0 14 14" aria-hidden="true"><rect x="1" y="3" width="12" height="8.5" rx="1" fill="var(--gold)"/><path d="M1.5 3.5 7 8l5.5-4.5" fill="none" stroke="#fff" stroke-width="1.1"/></svg>
        <span>info@<span class="accent">belsoravingroup</span>.com</span>
      </li>
      <li>
        <svg viewBox="0 0 14 14" aria-hidden="true"><circle cx="7" cy="7" r="6" fill="var(--gold)"/></svg>
        <span>www.<span class="accent">belsoravingroup</span>.com</span>
      </li>
    </ul>

    <div class="band"><div class="band__rule"></div><div class="band__fill"></div></div>
  </section>

</main>
</body>
</html>
```